Business Card Design

We are a Sydney based bespoke Concierge company, providing hospitality services including Concierge staffing, catering, home dining, events, delivery, passwright, and manage desks in residential apartment services. Our website goes into more detail.

Target Market(s)

corporate clients, upscale residential clients, executives,

Industry/Entity Type

Hospitality

Contact Information for Business Card

David SouthwellDirector of Operations & Customer Experience
Larkmoor Concierge
W:www.larkmoorconcierge.net;
E;martin@larkmoorconcierge.net
M: 0491 570 213

Font styles to use
Serif

Colors
3176b5
85cae6
d2a4cc
6b449b

Requirements
Must have
• Business name
• Name
• Title
• Tel
• Email
• Website
Nice to have
• Back - facebook , twitter, instagram

```html
<!DOCTYPE html>
<html lang="en">
<head>
<meta charset="utf-8">
<title>Larkmoor Concierge – Business Card</title>
<link rel="stylesheet" href="https://fonts.googleapis.com/css2?family=Tinos:wght@400&display=swap">
<style>
  :root {
    --purple: #6b449b;
    --title-purple: #6a4a9e;
    --blue: #3176b5;
    --white: #ffffff;
    --page: #e9e7ec;
    --shadow: rgba(40, 30, 60, 0.18);
  }
  * { margin: 0; padding: 0; box-sizing: border-box; }
  html, body {
    width: 1200px; height: 900px; overflow: hidden;
    background: var(--page);
    font-family: "Tinos", "Times New Roman", serif;
  }
  .canvas { position: relative; width: 1200px; height: 900px; }
  .card {
    position: absolute; left: 250px; width: 700px; height: 400px;
    background: var(--white);
    box-shadow: 0 6px 22px var(--shadow);
    overflow: hidden;
  }
  .card--front { top: 30px; }
  .card--back { top: 470px; }

  .front-band { position: absolute; inset: 0; }

  .holder { position: absolute; left: 34px; top: 44px; color: var(--white); }
  .holder__name { font-size: 27px; line-height: 1.1; }
  .holder__title { font-size: 17px; line-height: 1.25; margin-top: 6px; }

  .contact {
    position: absolute; left: 34px; bottom: 26px;
    list-style: none; color: var(--white); font-size: 17px;
  }
  .contact__item { display: flex; align-items: center; gap: 10px; line-height: 1.45; }
  .contact__icon { width: 15px; height: 15px; flex: none; }

  .brand { position: absolute; left: 392px; top: 108px; color: var(--title-purple); }
  .brand__name {
    font-size: 46px; line-height: 0.92; font-weight: 400;
    text-transform: uppercase; letter-spacing: 0.5px;
  }
  .brand__services { font-size: 13.5px; line-height: 1.3; margin-top: 12px; }

  .back-name {
    position: absolute; left: 0; right: 0; top: 168px; text-align: center;
    color: var(--title-purple); font-size: 48px; font-weight: 400;
    text-transform: uppercase; letter-spacing: 0.5px;
  }
  .social { position: absolute; left: 38px; bottom: 30px; display: flex; gap: 12px; }
  .social__dot { width: 14px; height: 14px; border-radius: 50%; background: var(--blue); }
</style>
</head>
<body>
<main class="canvas">

  <section class="card card--front" aria-label="Business card front">
    <svg class="front-band" viewBox="0 0 700 400" width="700" height="400" aria-hidden="true">
      <path d="M0 0 H282 C292 150 334 300 400 400 H0 Z" fill="var(--purple)"/>
      <path d="M250 0 C260 150 300 300 358 400 L370 400 C312 300 274 150 263 0 Z" fill="var(--white)"/>
    </svg>

    <div class="holder">
      <p class="holder__name">Martin Ashgrove</p>
      <p class="holder__title">Director of Operations &amp;<br>Customer Experience</p>
    </div>

    <ul class="contact">
      <li class="contact__item">
        <svg class="contact__icon" viewBox="0 0 16 16" aria-hidden="true">
          <rect width="16" height="16" rx="2" fill="var(--white)"/>
          <path d="M5 3.5 l2 2 -1 1.4 c.8 1.5 1.7 2.4 3.2 3.2 l1.4-1 2 2 -1.3 1.6 C7.8 12.3 3.7 8.2 3.5 4.8 Z" fill="var(--purple)"/>
        </svg>
        0491 570 213
      </li>
      <li class="contact__item">
        <svg class="contact__icon" viewBox="0 0 16 16" aria-hidden="true">
          <rect width="16" height="16" rx="2" fill="var(--white)"/>
          <rect x="3" y="4.5" width="10" height="7" fill="none" stroke="var(--purple)" stroke-width="1.3"/>
          <path d="M3 4.5 L8 8.8 L13 4.5" fill="none" stroke="var(--purple)" stroke-width="1.3"/>
        </svg>
        martin@larkmoorconcierge.net
      </li>
      <li class="contact__item">
        <svg class="contact__icon" viewBox="0 0 16 16" aria-hidden="true">
          <rect width="16" height="16" rx="2" fill="var(--white)"/>
          <circle cx="8" cy="8" r="4.8" fill="none" stroke="var(--purple)" stroke-width="1.2"/>
          <path d="M3.2 8 H12.8 M8 3.2 C5.8 6 5.8 10 8 12.8 M8 3.2 C10.2 6 10.2 10 8 12.8" fill="none" stroke="var(--purple)" stroke-width="1"/>
        </svg>
        www.larkmoorconcierge.net
      </li>
    </ul>

    <div class="brand">
      <h1 class="brand__name">Larkmoor<br>Concierge</h1>
      <p class="brand__services">Concierge staffing, catering, home dining<br>events, delivery, passwright<br>and manage desks in residential apartment services</p>
    </div>
  </section>

  <section class="card card--back" aria-label="Business card back">
    <h2 class="back-name">Larkmoor Concierge</h2>
    <div class="social" aria-label="Social media">
      <span class="social__dot"></span>
      <span class="social__dot"></span>
      <span class="social__dot"></span>
    </div>
  </section>

</main>
</body>
</html>
```